Financial Services Consultant needs a business card

We need a business card for a new consulting company based in Melbourne called
"Korvane Metrics". Tagline is Measure, Monitor, Save
We would like to see business card designs that are in line with the minimal style of the website www.korvane-metrics-example.com
The font I have used on the website is Proxima Nova and would like the same or similar font used on the business card with a minimal design in line with the website Two sided with "KORVANE METRICS" MEASURE, MONITOR, SAVE on one side and name, title and contact details on the otther
Updates

Hi All, thanks for your submissions, much appreciated.

I have recently added some colour to my webiste, it is hex #3a7b74 for those that wish to use it
Thanks

Hi all

thanks very much for your design submissions I am very impressed and they are much appreciated.

Interms of general feedback please find below;

Colour: I am trying to stick to a minimal design and colour scheme for my website which is still under construction, up to 3 colours( www.korvane-metrics-example.com) it is currently black and white with a small amount of blue/green but I am open to suggestion/interpretations for a consulting company.

Card: I dont mind if it has rounded edges or straight, I was thinking about using a letterpress card if possible

Detail: the detail on the card will include; Name, Title, Mobile, Personal Email, Business Email,Web,Business Address

Once again thanks for submissions

Industry/Entity Type

Business

```html
<!DOCTYPE html>
<html lang="en">
<head>
<meta charset="utf-8">
<title>Korvane Metrics — Business Card Front</title>
<link rel="stylesheet" href="https://fonts.googleapis.com/css2?family=Montserrat:wght@400;700&display=swap">
<style>
  :root {
    --page-bg: #ffffff;
    --card-white: #ffffff;
    --brand-green: #33916a;
    --ink-black: #000000;
    --ink-white: #ffffff;
  }
  html, body {
    margin: 0;
    padding: 0;
    width: 1200px;
    height: 1000px;
    overflow: hidden;
    background: var(--page-bg);
  }
  .canvas {
    position: relative;
    width: 1200px;
    height: 1000px;
  }
  .card-front {
    position: absolute;
    left: 76px;
    top: 200px;
    width: 1050px;
    height: 600px;
    display: block;
  }
  .card-base { fill: var(--card-white); }
  .green-field { fill: var(--brand-green); }
  .brand-name {
    font-family: "Montserrat", sans-serif;
    font-weight: 700;
    font-size: 64px;
  }
  .tagline {
    font-family: "Montserrat", sans-serif;
    font-weight: 400;
    font-size: 42px;
    letter-spacing: 27px;
  }
  .ink-dark { fill: var(--ink-black); }
  .ink-light { fill: var(--ink-white); }
</style>
</head>
<body>
<main class="canvas">
  <svg class="card-front" viewBox="0 0 1050 600" xmlns="http://www.w3.org/2000/svg" aria-label="Korvane Metrics business card, front side">
    <defs>
      <clipPath id="card-outline">
        <path d="M45 0 H1050 V600 H45 A45 45 0 0 1 0 555 V45 A45 45 0 0 1 45 0 Z"/>
      </clipPath>
      <clipPath id="green-area">
        <polygon points="0,0 96,0 954,600 0,600"/>
      </clipPath>
    </defs>

    <g clip-path="url(#card-outline)">
      <rect class="card-base" x="0" y="0" width="1050" height="600"/>
      <polygon class="green-field" points="0,0 96,0 954,600 0,600"/>

      <!-- Lettering on the white field -->
      <g class="ink-dark">
        <text class="brand-name" x="182" y="258" textLength="800" lengthAdjust="spacing">KORVANE METRICS</text>
        <text class="tagline" x="182" y="383">&gt;MEASURE</text>
        <text class="tagline" x="442" y="441">&gt;MONITOR</text>
        <text class="tagline" x="666" y="501" style="letter-spacing:34px">&gt;SAVE</text>
      </g>

      <!-- Same lettering reversed out of the green field -->
      <g class="ink-light" clip-path="url(#green-area)" aria-hidden="true">
        <text class="brand-name" x="182" y="258" textLength="800" lengthAdjust="spacing">KORVANE METRICS</text>
        <text class="tagline" x="182" y="383">&gt;MEASURE</text>
        <text class="tagline" x="442" y="441">&gt;MONITOR</text>
        <text class="tagline" x="666" y="501" style="letter-spacing:34px">&gt;SAVE</text>
      </g>
    </g>
  </svg>
</main>
</body>
</html>
```